Branvique needs a business Card Design

We are looking for a business card Design for our new Managed Service Provider Company, Branvique. Branvique encompasses everything IT for the average medium sized business. Our primary services are help desk support, cyber-security (malware and ransomware protection), and Disaster Recovery systems. We would like the design to have a very clean and professional look, with a very minimalist feel.

Target Market(s)

Medium to large sized businesses

Industry/Entity Type

It Service

Contact Information for Business Card

Name GoesHere
name@branvique.com
O: 555-382-6047
C: 555-731-5820

Font styles to use
Other font styles liked:
• Poppins Font Only Please

Colors

Designer to choose only greyscale colors for use in the design.

Requirements
Must have
• Logo included
Nice to have
• Cutting Edge, innovative, minimalistic, elegant

```html
<!DOCTYPE html>
<html lang="en">
<head>
<meta charset="utf-8">
<title>Branvique — Business Card</title>
<link href="https://fonts.googleapis.com/css2?family=Poppins:wght@300;400;500&display=swap" rel="stylesheet">
<style>
  :root {
    --backdrop: #e4e4e4;
    --card-white: #ffffff;
    --charcoal: #262626;
    --ink: #1e1e1e;
    --muted: #5f5f5f;
    --on-dark: #ffffff;
  }
  * { margin: 0; padding: 0; box-sizing: border-box; }
  html, body {
    width: 1200px;
    height: 714px;
    overflow: hidden;
    background: var(--backdrop);
    font-family: "Poppins", sans-serif;
  }
  .stage {
    position: relative;
    width: 1200px;
    height: 714px;
  }
  .card {
    position: absolute;
    top: 241px;
    height: 234px;
    box-shadow: 0 3px 10px rgba(0, 0, 0, 0.22);
  }
  .card--front {
    left: 189px;
    width: 406px;
    background: var(--card-white);
  }
  .card--back {
    left: 604px;
    width: 410px;
    background: var(--charcoal);
  }
  .brand-mark {
    position: absolute;
    left: 76px;
    top: 37px;
    width: 14px;
    height: 14px;
    background: var(--charcoal);
  }
  .brand-name {
    position: absolute;
    left: 20px;
    top: 75px;
    font-size: 14px;
    line-height: 20px;
    font-weight: 400;
    letter-spacing: 0.42em;
    color: var(--ink);
    text-transform: uppercase;
  }
  .person-name {
    position: absolute;
    left: 20px;
    top: 113px;
    font-size: 15px;
    line-height: 22px;
    font-weight: 500;
    color: var(--ink);
    text-transform: uppercase;
  }
  .person-title {
    position: absolute;
    left: 20px;
    top: 133px;
    font-size: 11.5px;
    line-height: 16px;
    font-weight: 300;
    color: var(--muted);
  }
  .contact-list {
    position: absolute;
    left: 20px;
    top: 165px;
    list-style: none;
  }
  .contact-item {
    display: flex;
    align-items: center;
    gap: 4px;
    height: 16.5px;
    font-size: 10.5px;
    font-weight: 300;
    color: var(--ink);
  }
  .contact-icon {
    width: 9px;
    height: 9px;
    fill: var(--ink);
    flex: none;
  }
  .back-wordmark {
    position: absolute;
    left: 124px;
    top: 168px;
    font-size: 26px;
    line-height: 36px;
    font-weight: 400;
    letter-spacing: 0.45em;
    color: var(--on-dark);
    text-transform: uppercase;
    white-space: nowrap;
  }
</style>
</head>
<body>
<main class="stage">
  <section class="card card--front" aria-label="Business card front">
    <span class="brand-mark" aria-hidden="true"></span>
    <p class="brand-name">Branvique</p>
    <h1 class="person-name">Daniel Harwick</h1>
    <p class="person-title">President</p>
    <ul class="contact-list">
      <li class="contact-item">
        <svg class="contact-icon" viewBox="0 0 24 24" aria-hidden="true"><path d="M6.6 10.8a15.1 15.1 0 0 0 6.6 6.6l2.2-2.2a1 1 0 0 1 1-.25 11.4 11.4 0 0 0 3.6.57 1 1 0 0 1 1 1V20a1 1 0 0 1-1 1A17 17 0 0 1 3 4a1 1 0 0 1 1-1h3.5a1 1 0 0 1 1 1c0 1.25.2 2.45.57 3.57a1 1 0 0 1-.25 1z"/></svg>
        555-382-6047
      </li>
      <li class="contact-item">
        <svg class="contact-icon" viewBox="0 0 24 24" aria-hidden="true"><path d="M7 1h10a2 2 0 0 1 2 2v18a2 2 0 0 1-2 2H7a2 2 0 0 1-2-2V3a2 2 0 0 1 2-2zm0 3v14h10V4zm5 15.5a1.2 1.2 0 1 0 0 2.4 1.2 1.2 0 0 0 0-2.4z"/></svg>
        555-731-5820
      </li>
      <li class="contact-item">
        <svg class="contact-icon" viewBox="0 0 24 24" aria-hidden="true"><path d="M2 5h20v14H2zm2 2v.5l8 5 8-5V7zm0 2.9V17h16V9.9l-8 5z"/></svg>
        name@branvique.com
      </li>
    </ul>
  </section>

  <section class="card card--back" aria-label="Business card back">
    <p class="back-wordmark">Branvique</p>
  </section>
</main>
</body>
</html>
```